Unmanned Aerial Systems/Drones Postcard Design

Harbor Mile Aerial is a new local business providing photography and videography for various industries; Real Estate, construction, property management, agriculture, legal, property inspections, building survey and more.Harbor Mile Aerial is authorized and approved for commercial operations by the National Airspace Registry Bureau.Unauthorized operators maybe subject to large fines and even prosecution.Harbor Mile aerial only uses licensed NARB pilots and an additional visual observer for enhanced safety on each project.

Industry/Entity Type

Business

Requirements
Must have
• The NARB logo connected to the statement "Harbor Mile Aerial is authorized and approved for commercial operations by the National Airspace Registry Bureau"
Nice to have
• The sunset picture should be the focus as it grabs more attention.
Should not have
• Must not be a generic design, I am looking for something with more style

```html
<!DOCTYPE html>
<html lang="en">
<head>
<meta charset="utf-8">
<title>Harbor Mile Aerial Postcard</title>
<link rel="stylesheet" href="https://fonts.googleapis.com/css2?family=Roboto+Condensed:wght@400;700&family=Roboto:wght@300;400&display=swap">
<style>
  :root {
    --page: #e4e4e4;
    --white: #ffffff;
    --off-white: #f1f1f1;
    --sky: #1ea6ec;
    --ocean: #0d6fb8;
    --navy: #1f4a6e;
    --heading-blue: #1d5b8c;
    --text-dark: #2c2c2c;
    --link-blue: #1b55a6;
    --red: #d7363c;
    --seal-ring: #eaa3a9;
    --seal-core: #1d2f6b;
  }
  * { box-sizing: border-box; margin: 0; padding: 0; }
  html, body {
    width: 1125px; height: 1200px; overflow: hidden;
    background: var(--page);
  }
  .postcard {
    position: absolute; left: 30px; top: 218px;
    width: 1065px; height: 764px;
    overflow: hidden; background: var(--white);
    box-shadow: 0 6px 18px rgba(0,0,0,.25);
  }
  .postcard__art { position: absolute; inset: 0; width: 100%; height: 100%; }

  .pilot-panel {
    position: absolute; left: 42px; top: 492px; width: 410px; height: 272px;
    background: linear-gradient(180deg, var(--sky) 0%, #138ad6 100%);
    border-right: 8px solid var(--ocean);
    color: var(--white); text-align: center;
    font-family: "Roboto Condensed", sans-serif; font-weight: 700;
    padding-top: 44px;
  }
  .pilot-panel__line { font-size: 39px; line-height: 50px; text-transform: uppercase; }
  .pilot-panel__line--big { font-size: 60px; line-height: 62px; }
  .pilot-panel__note { font-size: 16px; line-height: 20px; font-weight: 400; margin-top: 8px; text-transform: uppercase; }

  .services {
    position: absolute; right: 42px; top: 428px; width: 560px;
    text-align: right;
  }
  .services__title {
    font-family: "Roboto Condensed", sans-serif; font-weight: 400;
    font-size: 31px; line-height: 40px; color: var(--heading-blue);
  }
  .services__subtitle {
    font-family: "Roboto", sans-serif; font-weight: 400;
    font-size: 24px; line-height: 30px; color: var(--navy); margin-top: 10px;
  }
  .services__list {
    font-family: "Roboto", sans-serif; font-weight: 300;
    font-size: 23px; line-height: 30px; color: var(--text-dark); margin-top: 10px;
  }
  .services__approval {
    font-family: "Roboto Condensed", sans-serif; font-weight: 400;
    font-size: 20px; line-height: 30px; color: var(--link-blue); margin-top: 12px;
  }

  .contact-bar {
    position: absolute; left: 453px; top: 719px; width: 612px; height: 36px;
    background: var(--navy); color: var(--white);
    font-family: "Roboto", sans-serif; font-size: 21px;
    display: flex; align-items: center;
  }
  .contact-bar__item { display: flex; align-items: center; gap: 12px; }
  .contact-bar__item--email { padding-left: 22px; width: 330px; }
  .contact-bar__divider { width: 4px; height: 46px; background: var(--white); transform: skewX(-22deg); margin-right: 28px; }
  .contact-bar__icon { width: 28px; height: 28px; }
</style>
</head>
<body>
<div class="postcard">
  <svg class="postcard__art" viewBox="0 0 769 552" preserveAspectRatio="none">
    <defs>
      <linearGradient id="photo-tone" x1="0" y1="0" x2="0" y2="1">
        <stop offset="0" stop-color="#5e7a4a"/>
        <stop offset="0.45" stop-color="#7a9a5c"/>
        <stop offset="1" stop-color="#5c8a3c"/>
      </linearGradient>
    </defs>
    <rect class="hero-photo" role="img" aria-label="Photograph of a white quadcopter drone with camera hovering over a park lawn" x="0" y="0" width="769" height="552" fill="url(#photo-tone)"/>
    <path class="wave wave--blue" fill="var(--ocean)" d="M0,268 C140,335 330,320 620,228 C680,210 740,230 769,262 L769,552 L0,552Z"/>
    <path class="wave wave--gap" fill="var(--white)" d="M0,294 C150,358 340,344 620,250 C688,228 740,246 769,276 L769,552 L0,552Z"/>
    <path class="wave wave--red" fill="var(--red)" d="M0,302 C150,366 340,352 620,258 C690,235 740,252 769,282 L769,552 L0,552Z"/>
    <path class="wave wave--body" fill="var(--white)" d="M0,334 C160,396 360,372 620,276 C690,252 740,262 769,290 L769,552 L0,552Z"/>
    <rect class="margin-strip" x="0" y="355" width="30" height="197" fill="var(--off-white)"/>
    <g class="registry-seal">
      <circle cx="631" cy="221" r="82" fill="var(--seal-ring)"/>
      <circle cx="631" cy="221" r="73" fill="var(--white)"/>
      <circle cx="631" cy="221" r="68" fill="var(--seal-core)"/>
    </g>
  </svg>

  <div class="pilot-panel">
    <p class="pilot-panel__line">Harbor Mile Aerial</p>
    <p class="pilot-panel__line">Only uses licensed</p>
    <p class="pilot-panel__line pilot-panel__line--big">NARB Pilots</p>
    <p class="pilot-panel__note">And an additional visual observer<br>for enhanced safety on each project.</p>
  </div>

  <div class="services">
    <h1 class="services__title">Harbor Mile Aerial Providing</h1>
    <p class="services__subtitle">Photography &amp; Videography<br>For Various Industries</p>
    <p class="services__list">Real Estate, Construction, Property Management,<br>Agriculture, Legal, Property Inspections<br>Building Survey And More.</p>
    <p class="services__approval">Harbor Mile Aerial Is Authorized And Approved For Commercial<br>Operations By The National Airspace Registry Bureau.</p>
  </div>

  <div class="contact-bar">
    <div class="contact-bar__item contact-bar__item--email">
      <svg class="contact-bar__icon" viewBox="0 0 28 28" fill="none" stroke="#fff" stroke-width="1.8"><rect x="3" y="7" width="22" height="15"/><path d="M3 7 L14 16 L25 7"/></svg>
      <span>hello@harbormileaerial.com</span>
    </div>
    <div class="contact-bar__divider"></div>
    <div class="contact-bar__item">
      <svg class="contact-bar__icon" viewBox="0 0 28 28" fill="none" stroke="#fff" stroke-width="1.8"><circle cx="14" cy="14" r="12"/><path d="M10 8 L12 8 L13 11 L11.5 12.5 C12.5 14.5 13.5 15.5 15.5 16.5 L17 15 L20 16 L20 18 C20 19 19 20 18 20 C12 19.5 8.5 16 8 10 C8 9 9 8 10 8Z" fill="#fff" stroke="none"/></svg>
      <span>555-014-2276</span>
    </div>
  </div>
</div>
</body>
</html>
```